BASIC website restyle: graphic + coding

I need a restyle of our present website. Same contents, but better graphic.
It will be temporary until we'll have defined the strategy and so we'll have the definitive one.
I would need a fast job including coding.

I uploaded some picture that you're free to use.
I also extended of 1 day, no more extensions will be possible.

```html
<!DOCTYPE html>
<html lang="en">
<head>
<meta charset="utf-8">
<title>Verdanet</title>
<link href="https://fonts.googleapis.com/css2?family=Open+Sans:wght@400;600;700&display=swap" rel="stylesheet">
<style>
:root{
  --green:#008c44;
  --green-bright:#1a9d4f;
  --text-dark:#3a4350;
  --white:#ffffff;
  --footer-base:#3a4350;
  --band:rgba(225,232,236,0.55);
}
*{margin:0;padding:0;box-sizing:border-box}
html,body{width:1200px;height:778px;overflow:hidden;background:var(--white)}
body{font-family:"Open Sans",Arial,sans-serif;position:relative}
.top-rule{position:absolute;left:0;top:0;width:1200px;height:3px;background:var(--green)}
.site-header{position:absolute;left:0;top:3px;width:1200px;height:87px;background:var(--white)}
.brand{position:absolute;left:207px;top:22px;font-size:36px;font-weight:700;color:var(--green);letter-spacing:-1px;line-height:1}
.main-nav{position:absolute;left:535px;top:0;height:87px;display:flex}
.main-nav a{display:block;height:87px;line-height:87px;font-size:12.5px;color:var(--text-dark);text-decoration:none;padding:0 15.5px}
.main-nav a.active{background:var(--green);color:var(--white);padding:0 21px}
.hero{position:absolute;left:0;top:90px;width:1200px;height:596px;overflow:hidden}
.hero-photo{position:absolute;inset:0;background:
  radial-gradient(ellipse at 30% 25%,#c9e2b2 0%,rgba(201,226,178,0) 45%),
  radial-gradient(ellipse at 70% 60%,#8fcf3a 0%,rgba(143,207,58,0) 50%),
  linear-gradient(180deg,#a6c690 0%,#7cbf3d 45%,#4f9a26 75%,#3f7f1f 100%)}
.hero-title{position:absolute;left:246px;top:159px;width:336px;height:58px;background:var(--green-bright);color:var(--white);font-size:27px;font-weight:700;line-height:58px;text-align:center;letter-spacing:0.3px}
.slide-arrow{position:absolute;top:159px;width:57px;height:57px}
.slide-arrow.prev{left:151px}
.slide-arrow.next{left:992px}
.feature-band{position:absolute;left:0;top:387px;width:1200px;height:209px;background:var(--band)}
.feature-card{position:absolute;top:424px;width:374px;height:140px;color:var(--white)}
.feature-card.fire{left:208px}
.feature-card.agri{left:617px}
.card-photo{position:absolute;inset:0}
.fire .card-photo{background:linear-gradient(100deg,#3c4d63 0%,#4f6f96 40%,#7b8aa0 65%,#a3542a 100%)}
.agri .card-photo{background:linear-gradient(135deg,#3a2a1c 0%,#4f3a24 40%,#43502a 70%,#2e2418 100%)}
.card-thumb{position:absolute;left:17px;top:15px;width:105px;height:107px;border:5px solid rgba(200,200,200,0.85)}
.fire .card-thumb{background:linear-gradient(160deg,#4b4a3e,#9a9a92 55%,#6b5a3a)}
.agri .card-thumb{background:linear-gradient(160deg,#8f7b52,#c6c3bd 55%,#3f5f40)}
.card-title{position:absolute;left:140px;top:16px;font-size:21px;font-weight:400;line-height:26px}
.card-text{position:absolute;left:141px;top:44px;width:215px;font-size:11.5px;line-height:15.2px}
.card-more{position:absolute;left:142px;top:89px;width:73px;height:24px;background:var(--green);color:var(--white);font-size:12px;line-height:24px;text-align:center;text-decoration:none}
.site-footer{position:absolute;left:0;top:686px;width:1200px;height:85px;background:var(--green)}
.copyright{position:absolute;left:207px;top:26px;font-size:11.5px;color:var(--white)}
.social{position:absolute;left:915px;top:26px;display:flex;gap:15px}
.social span{display:block;width:14px;height:14px;border-radius:50%;background:var(--white)}
.footer-base{position:absolute;left:0;top:771px;width:1200px;height:7px;background:var(--footer-base)}
</style>
</head>
<body>
<div class="top-rule"></div>
<header class="site-header">
  <div class="brand">VERDANET</div>
  <nav class="main-nav">
    <a class="active" href="#">HOME</a>
    <a href="#">FIREWATCH</a>
    <a href="#">FIELDSENSE</a>
    <a href="#">TECHNOLOGY</a>
    <a href="#">CONTACT US</a>
  </nav>
</header>

<section class="hero">
  <div class="hero-photo" role="img" aria-label="Close-up photo of fresh green grass blades"></div>
  <h1 class="hero-title">INTERNET OF THINGS</h1>
  <svg class="slide-arrow prev" viewBox="0 0 57 57" aria-label="Previous slide">
    <circle cx="28.5" cy="28.5" r="28.5" fill="#1a9d4f" opacity="0.85"/>
    <polyline points="33,15 22,28.5 33,42" fill="none" stroke="#fff" stroke-width="1.6"/>
  </svg>
  <svg class="slide-arrow next" viewBox="0 0 57 57" aria-label="Next slide">
    <circle cx="28.5" cy="28.5" r="28.5" fill="#1a9d4f" opacity="0.85"/>
    <polyline points="24,15 35,28.5 24,42" fill="none" stroke="#fff" stroke-width="1.6"/>
  </svg>
  <div class="feature-band"></div>

  <article class="feature-card fire">
    <div class="card-photo" role="img" aria-label="Photo of a forest fire with smoke over burning trees"></div>
    <div class="card-thumb" role="img" aria-label="Photo of a wireless sensor mounted on a tree"></div>
    <h2 class="card-title">Forest fires</h2>
    <p class="card-text">Lorem Ipsum is simply dummy text of the printing and typesetting industry. Lorem Ipsum has been the industry's</p>
    <a class="card-more" href="#">More</a>
  </article>

  <article class="feature-card agri">
    <div class="card-photo" role="img" aria-label="Photo of cultivated field rows with young crops"></div>
    <div class="card-thumb" role="img" aria-label="Photo of a sensor circuit board"></div>
    <h2 class="card-title">Agriculture</h2>
    <p class="card-text">Lorem Ipsum is simply dummy text of the printing and typesetting industry. Lorem Ipsum has been the industry's</p>
    <a class="card-more" href="#">More</a>
  </article>
</section>

<footer class="site-footer">
  <p class="copyright">Copyright © 2013 All right reserved by verdanet.com</p>
  <div class="social" aria-label="Social links"><span></span><span></span><span></span></div>
</footer>
<div class="footer-base"></div>
</body>
</html>
```